VEHICLE WRAP

2022 VORLAND TEK CARGOLINE XL MUST HAVE UNIFIED LOOK OPEN TO DIFFERENT LOOKS BUT MUST BE UNIFIES TO THE OTHER TRCUKS WE HAVE IN THE BUSINESS PLEASE SEE PHOTOS BUT SERVICES SAME AS BRISKEN LOCKSMITH TRUCK

Industry/Entity Type

LOCKSMITH

Font styles to use
Serif
Sans Serif

Colors
EB3D1F
EC4F4E
F09395
F8D3D4
FCEDEE

Requirements
Must have
• SAME COLORS DARK GREY RED
Should not have
• NO NEW COLORS

```html
<!DOCTYPE html>
<html lang="en">
<head>
<meta charset="utf-8">
<title>Brisken Locksmith — Cargoline XL Wrap</title>
<link href="https://fonts.googleapis.com/css2?family=Rubik:wght@500;700;800&display=swap" rel="stylesheet">
<style>
  :root{
    --red:#EB3D1F;
    --red-soft:#EC4F4E;
    --dark:#2a2a2a;
    --grey:#3a3a3a;
    --white:#ffffff;
    --body:#f4f4f4;
    --stage:#e9e9ea;
    --glass:#1f2326;
    --steel:#b9bcc0;
  }
  html,body{margin:0;padding:0;width:1200px;height:1200px;overflow:hidden;background:var(--stage);}
  .wrap-board{width:1200px;height:1200px;display:block;}
  .wrap-board text{font-family:"Rubik",sans-serif;font-weight:700;}
  .pill-text{fill:var(--white);font-size:25px;}
  .site{fill:var(--dark);font-size:28px;}
  .site-accent{fill:var(--red);}
  .sectors{fill:var(--dark);font-size:29px;}
  .sector-dot{fill:var(--red);}
  .phone{fill:var(--white);font-size:46px;}
  .address{fill:var(--dark);font-size:27px;}
  .brand-name{fill:var(--dark);font-size:42px;font-weight:800;}
  .badge-num{fill:var(--red);font-size:46px;font-weight:800;}
  .badge-num-dark{fill:var(--dark);}
  .badge-label{fill:var(--dark);font-size:18px;}
</style>
</head>
<body>
<svg class="wrap-board" viewBox="0 300 1932 1200" xmlns="http://www.w3.org/2000/svg" aria-label="Brisken Locksmith cargo van side wrap">
  <defs>
    <clipPath id="van-body">
      <path d="M92 622 Q95 604 120 604 L1262 604 Q1300 604 1330 622 L1560 745 Q1640 800 1720 920 L1800 990 Q1860 1010 1872 1060 L1878 1180 Q1878 1230 1830 1232 L70 1232 Q62 1232 62 1210 L70 1080 Z"/>
    </clipPath>
  </defs>

  <g class="van">
    <path class="van-shell" fill="var(--body)" d="M92 622 Q95 604 120 604 L1262 604 Q1300 604 1330 622 L1560 745 Q1640 800 1720 920 L1800 990 Q1860 1010 1872 1060 L1878 1180 Q1878 1230 1830 1232 L70 1232 Q62 1232 62 1210 L70 1080 Z"/>

    <g class="wrap-graphics" clip-path="url(#van-body)">
      <path class="red-sweep" fill="var(--red)" d="M220 600 L860 600 L860 1240 L840 1240 Q820 1080 760 1010 Q620 850 420 740 Q300 680 150 690 L150 660 Q200 620 220 600 Z"/>
      <path class="red-sweep-lower" fill="var(--red)" d="M840 600 L1010 600 L1320 1240 L870 1240 Z"/>
      <path class="dark-band" fill="var(--dark)" d="M980 600 L1150 600 L1310 1240 L1150 1240 Z"/>
      <path class="red-band" fill="var(--red)" d="M1150 600 L1200 600 Q1260 900 1340 1240 L1300 1240 Z"/>
      <path class="white-band" fill="var(--body)" d="M1200 600 L1262 600 L1262 1180 L1330 1240 L1340 1240 Q1260 900 1200 600 Z"/>
      <path class="dark-corner" fill="var(--dark)" d="M1262 1150 L1500 1150 L1500 1240 L1262 1240 Z"/>
      <path class="red-base" fill="var(--red)" d="M880 1200 L1340 1200 L1320 1240 L880 1240 Z"/>
    </g>

    <path class="rear-bumper" fill="var(--dark)" d="M62 1088 L360 1088 Q320 1130 318 1232 L68 1232 Q60 1232 60 1210 Z"/>
    <rect class="side-trim" x="615" y="1150" width="840" height="52" rx="6" fill="var(--grey)"/>
    <path class="front-bumper" fill="var(--dark)" d="M1720 1070 L1872 1050 L1878 1180 Q1878 1230 1830 1232 L1740 1232 Q1740 1120 1720 1070 Z"/>
    <rect class="tail-light" x="70" y="905" width="32" height="180" rx="10" fill="var(--red-soft)"/>

    <line x1="857" y1="606" x2="857" y2="1232" stroke="#cfcfcf" stroke-width="2"/>
    <line x1="1265" y1="606" x2="1265" y2="1232" stroke="#cfcfcf" stroke-width="2"/>
    <line x1="1605" y1="790" x2="1605" y2="1200" stroke="#cfcfcf" stroke-width="2"/>
    <rect class="slide-rail" x="420" y="918" width="430" height="14" rx="4" fill="var(--grey)"/>

    <path class="cab-window" fill="var(--glass)" d="M1312 760 Q1312 748 1326 748 L1440 748 L1555 800 Q1600 860 1630 955 L1330 955 Q1312 955 1312 940 Z"/>
    <rect class="mirror" x="1552" y="858" width="56" height="104" rx="14" fill="var(--dark)"/>
    <rect class="door-handle" x="1208" y="955" width="36" height="62" rx="12" fill="var(--dark)"/>
    <rect class="door-handle" x="1312" y="955" width="36" height="62" rx="12" fill="var(--dark)"/>
    <path class="headlamp" fill="#555" d="M1705 935 L1805 990 L1805 1030 L1720 1015 Z"/>

    <g class="wheel">
      <circle cx="450" cy="1220" r="108" fill="var(--dark)"/>
      <circle cx="450" cy="1220" r="66" fill="var(--steel)"/>
      <circle cx="450" cy="1220" r="20" fill="var(--grey)"/>
    </g>
    <g class="wheel">
      <circle cx="1640" cy="1220" r="108" fill="var(--dark)"/>
      <circle cx="1640" cy="1220" r="66" fill="var(--steel)"/>
      <circle cx="1640" cy="1220" r="20" fill="var(--grey)"/>
    </g>
  </g>

  <g class="service-list">
    <g class="service red">
      <circle cx="137" cy="724" r="9" fill="var(--red)"/><rect x="133" y="728" width="8" height="22" fill="var(--red)"/>
      <rect x="155" y="716" width="485" height="36" rx="18" fill="var(--red)"/>
      <text class="pill-text" x="172" y="743" textLength="456" lengthAdjust="spacingAndGlyphs">CARKEY • REMOTES • PROGRAMMING</text>
    </g>
    <g class="service dark">
      <circle cx="137" cy="772" r="9" fill="var(--dark)"/><rect x="133" y="776" width="8" height="22" fill="var(--dark)"/>
      <rect x="155" y="764" width="480" height="36" rx="18" fill="var(--dark)"/>
      <text class="pill-text" x="172" y="791" textLength="448" lengthAdjust="spacingAndGlyphs">ACCESS CONTROL • ALARM SYSTEM</text>
    </g>
    <g class="service red">
      <circle cx="137" cy="820" r="9" fill="var(--red)"/><rect x="133" y="824" width="8" height="22" fill="var(--red)"/>
      <rect x="155" y="812" width="598" height="36" rx="18" fill="var(--red)" stroke="var(--white)" stroke-width="2"/>
      <text class="pill-text" x="172" y="839" textLength="566" lengthAdjust="spacingAndGlyphs">HIGH SECURIY LOCKS • HANDICAP OPERATOR</text>
    </g>
    <g class="service dark">
      <circle cx="137" cy="868" r="9" fill="var(--dark)"/><rect x="133" y="872" width="8" height="22" fill="var(--dark)"/>
      <rect x="155" y="860" width="595" height="36" rx="18" fill="var(--dark)"/>
      <text class="pill-text" x="172" y="887" textLength="564" lengthAdjust="spacingAndGlyphs">KEYLESS ENTRY LOCKS • SAFES • HARDWARE</text>
    </g>
  </g>

  <text class="site" x="164" y="930" textLength="214" lengthAdjust="spacingAndGlyphs">BRISKLOCK<tspan class="site-accent">.COM</tspan></text>
  <text class="sectors" x="164" y="998" textLength="620" lengthAdjust="spacingAndGlyphs">RESIDENTIAL<tspan class="sector-dot"> • </tspan>COMMERCIAL<tspan class="sector-dot"> • </tspan>AUTOMOTIVE</text>

  <g class="brand">
    <circle cx="940" cy="765" r="152" fill="var(--white)" stroke="var(--dark)" stroke-width="22"/>
    <text class="brand-name" x="940" y="756" text-anchor="middle" textLength="170" lengthAdjust="spacingAndGlyphs">BRISKEN</text>
    <text class="brand-name" x="940" y="806" text-anchor="middle" textLength="230" lengthAdjust="spacingAndGlyphs">LOCKSMITH</text>
  </g>

  <rect class="phone-pill" x="585" y="1068" width="513" height="64" rx="32" fill="var(--dark)" stroke="var(--white)" stroke-width="3"/>
  <text class="phone" x="608" y="1116" textLength="464" lengthAdjust="spacingAndGlyphs">613-555-LOCK (5625)</text>

  <text class="address" x="1384" y="1010" textLength="290" lengthAdjust="spacingAndGlyphs">2280 HARLOW RIDGE RD</text>

  <g class="emergency">
    <circle cx="1368" cy="1090" r="28" fill="var(--red)"/>
    <text class="badge-num" x="1340" y="1110" textLength="124" lengthAdjust="spacingAndGlyphs"><tspan class="badge-num-dark">24</tspan>/7</text>
    <text class="badge-label" x="1342" y="1140" textLength="108" lengthAdjust="spacingAndGlyphs">EMERGENCY</text>
  </g>
</svg>
</body>
</html>
```